Ductless Mini Split Business Website

Amber Kite Services is looking to design an eye catching educational website about installing Ductless mini splits.

Similar to this company.
https://www.cedarcoolair.com/

```html
<!DOCTYPE html>
<html lang="en">
<head>
<meta charset="utf-8">
<title>Amber Kite Services — Ductless System Experts</title>
<link rel="stylesheet" href="https://fonts.googleapis.com/css2?family=Montserrat:wght@400;500;600;700&family=Arvo:wght@700&family=Fredoka:wght@600&family=Lora:wght@500&display=swap">
<style>
:root{
  --navy:#1b3a63;
  --navy-deep:#13284a;
  --orange:#f08a00;
  --ink:#1d1d1d;
  --muted:#6b6b6b;
  --white:#ffffff;
  --pink:#e86a8e;
  --yellow:#f2d51c;
  --blue:#1f5fa8;
}
*{margin:0;padding:0;box-sizing:border-box}
html,body{width:1200px;height:4079px;overflow:hidden}
body{position:relative;font-family:'Montserrat',sans-serif;color:var(--ink);background:var(--white)}
.abs{position:absolute}
.topbar{left:0;top:0;width:1200px;height:83px;background:var(--navy)}
.topbar-title{left:0;width:1200px;top:28px;text-align:center;color:var(--white);font-family:'Lora',serif;font-size:25px;font-weight:500}
.topbar-call{left:970px;top:35px;color:#d6dde8;font-size:11.5px}
.topbar-call b{color:var(--white);font-weight:700}
.navbar{left:0;top:83px;width:1200px;height:67px;background:var(--white)}
.brand{left:50px;top:99px;display:flex;align-items:center;gap:10px;font-weight:700;font-size:20px;color:var(--ink)}
.brand-dot{width:36px;height:36px;border-radius:50%;background:var(--yellow)}
.nav-link{top:109px;font-size:13px;font-weight:500;color:var(--ink)}
.hero{left:0;top:150px;width:1200px;height:658px;background:linear-gradient(135deg,#6d6a68 0%,#4c4a4a 45%,#3a3532 75%,#56483a 100%)}
.hero-shade{left:0;top:150px;width:1200px;height:658px;background:rgba(20,20,25,.35)}
.hero-kicker{left:0;width:1200px;top:328px;text-align:center;color:var(--white);font-size:25px;font-weight:500}
.hero-rule{left:344px;top:362px;width:512px;height:3px;background:var(--orange)}
.hero-title{left:0;width:1200px;top:378px;text-align:center;color:var(--white);font-family:'Fredoka',sans-serif;font-weight:600;font-size:74px}
.btn{background:var(--orange);color:var(--white);font-weight:600;display:flex;align-items:center;justify-content:center;font-size:12px}
.about-title{left:84px;top:924px;font-family:'Arvo',serif;font-size:27px;color:var(--ink)}
.about-rule{left:84px;top:962px;width:370px;height:2px;background:var(--orange)}
.about-sub{left:84px;top:988px;width:380px;font-size:15px;font-weight:500;letter-spacing:1px;line-height:25px}
.about-text{left:84px;top:1050px;width:360px;font-size:12.5px;line-height:16.5px;color:#444}
.video{left:533px;top:914px;width:584px;height:326px;background:linear-gradient(120deg,#5d6670,#868b8f 50%,#4d5359);box-shadow:0 8px 22px rgba(0,0,0,.28)}
.section-title{left:0;width:1200px;text-align:center;font-size:30px;font-weight:500}
.help-rule{left:415px;top:1429px;width:370px;height:3px;background:var(--orange)}
.svc{width:238px;height:243px;box-shadow:0 4px 10px rgba(0,0,0,.2);overflow:hidden}
.svc-photo{position:absolute;inset:0;background:linear-gradient(180deg,#d9dadb 0%,#f1f1f0 40%,#8d8c8a 100%)}
.svc-photo.dark{background:linear-gradient(180deg,#3b3733 0%,#5a554f 40%,#2d2a27 100%)}
.svc-photo.warm{background:linear-gradient(180deg,#cfc6bb 0%,#b98d62 50%,#8c7866 100%)}
.svc-band{position:absolute;left:0;width:238px;top:136px;height:73px;background:var(--orange);color:var(--white);font-size:15px;font-weight:500;letter-spacing:1.2px;text-align:center;display:flex;align-items:center;justify-content:center;line-height:19px}
.why{width:240px}
.why-title{font-size:15.5px;font-weight:500;line-height:20px}
.why-text{font-size:11.5px;color:var(--muted);line-height:15px;margin-top:10px}
.why-rule{width:56px;height:2px;margin:18px 0 16px}
.testi{left:0;top:2598px;width:1200px;height:350px;background:linear-gradient(180deg,#8d9196,#c5c8ca 55%,#7f8285)}
.testi-shade{left:0;top:2598px;width:1200px;height:350px;background:rgba(30,30,35,.35)}
.testi-quote{left:0;width:1200px;top:2680px;text-align:center;color:var(--white);font-size:40px;font-weight:700;letter-spacing:2px}
.avatar{left:567px;top:2757px;width:56px;height:56px;border-radius:50%;background:#c9c9c9;border:2px solid var(--white)}
.testi-name{left:0;width:1200px;top:2834px;text-align:center;color:var(--white);font-size:13px;font-weight:600}
.dot{top:2898px;width:14px;height:14px;border-radius:50%;border:2px solid var(--white)}
.more-kicker{left:0;width:1200px;top:3083px;text-align:center;font-size:16px}
.more-rule{left:333px;top:3105px;width:534px;height:2px;background:var(--orange)}
.more-title{left:0;width:1200px;top:3120px;text-align:center;font-family:'Fredoka',sans-serif;font-size:30px;font-weight:600}
.card{width:238px;height:236px;background:var(--white);box-shadow:0 3px 12px rgba(0,0,0,.2)}
.card-photo{width:238px;height:136px}
.card-title{text-align:center;font-size:15.5px;font-weight:500;margin-top:22px}
.card-btn{width:146px;height:36px;margin:12px auto 0;font-size:14px;font-weight:600}
.footer{left:0;top:3614px;width:1200px;height:465px;background:var(--navy-deep)}
.foot-brand{left:30px;top:3688px;display:flex;align-items:center;gap:10px;color:var(--white);font-weight:700;font-size:20px}
.foot-col{color:var(--white);font-size:13px;line-height:29px}
.foot-col h4{font-size:15px;font-weight:500;margin-bottom:6px}
</style>
</head>
<body>
<header>
  <div class="abs topbar"></div>
  <div class="abs topbar-title">Your Ductless System Experts</div>
  <div class="abs topbar-call">Call Us Today: <b>999-999-9999</b></div>
  <div class="abs navbar"></div>
  <div class="abs brand"><span class="brand-dot"></span>Amber Kite</div>
  <nav>
    <span class="abs nav-link" style="left:403px">Home</span>
    <span class="abs nav-link" style="left:489px">About Us</span>
    <span class="abs nav-link" style="left:597px">Ductless Heat Pumps</span>
    <span class="abs nav-link" style="left:787px">FAQ</span>
    <span class="abs nav-link" style="left:862px">Financing</span>
    <span class="abs nav-link" style="left:974px">Reviews</span>
    <span class="abs nav-link" style="left:1076px">Contact Us</span>
  </nav>
</header>

<section>
  <div class="abs hero" role="img" aria-label="Photo of a smiling team gathered around a laptop"></div>
  <div class="abs hero-shade"></div>
  <div class="abs hero-kicker">LET AMBER KITE HEROES SHOW YOU HOW</div>
  <div class="abs hero-rule"></div>
  <h1 class="abs hero-title">Ductless Does It Better</h1>
  <div class="abs btn" style="left:516px;top:497px;width:167px;height:41px">Get In Touch With Us</div>
</section>

<section>
  <h2 class="abs about-title">Amber Kite Ductless Heroes</h2>
  <div class="abs about-rule"></div>
  <p class="abs about-sub">HELPING PORTLAND AND SURROUNDING AREAS GO DUCTLESS</p>
  <p class="abs about-text">Lorem ipsum dolor sit amet, consectetur adipiscing elit. At auctor at dui mi. Ultricies nulla tellus convallis aliquet augue consequat. Parturient sem molestie tempus ultrices enim vel ut nibh orci. Ac ornare sagittis aliquam tristique pellentesque quam. Interdum volutpat dictumst viverra amet. Vitae in auctor volutpat proin quam pellentesque.</p>
  <div class="abs btn" style="left:85px;top:1195px;width:133px;height:33px">Learn More</div>
  <div class="abs video" role="img" aria-label="Video still of a team meeting with sticky notes on the wall"></div>
  <svg class="abs" style="left:808px;top:1055px" width="42" height="46" viewBox="0 0 42 46"><path d="M2 2 L40 23 L2 44 Z" fill="#fff"/></svg>
</section>

<section>
  <h2 class="abs section-title" style="top:1390px">HOW CAN WE HELP YOU</h2>
  <div class="abs help-rule"></div>

  <div class="abs svc" style="left:83px;top:1484px"><div class="svc-photo" role="img" aria-label="Photo of a white kitchen"></div><div class="svc-band">BASEBOARD HEAT<br>REPLACEMENT</div></div>
  <div class="abs svc" style="left:348px;top:1484px"><div class="svc-photo" role="img" aria-label="Photo of a kitchen with pendant lamp"></div><div class="svc-band" style="top:118px;height:93px">DUCTLESS FOR<br>ADDITIONAL AND<br>MODELS</div></div>
  <div class="abs svc" style="left:614px;top:1484px"><div class="svc-photo" role="img" aria-label="Photo of a bright kitchen with chandelier"></div><div class="svc-band">DUCTLESS HEAT<br>PUNP FAQ</div></div>
  <div class="abs svc" style="left:880px;top:1484px"><div class="svc-photo dark" role="img" aria-label="Photo of a dark modern kitchen"></div><div class="svc-band">DUCTLESS<br>INSTALLATION</div></div>

  <div class="abs svc" style="left:83px;top:1755px"><div class="svc-photo" role="img" aria-label="Photo of a kitchen with ceiling lights"></div><div class="svc-band">BASEBOARD HEAT<br>REPLACEMENT</div></div>
  <div class="abs svc" style="left:348px;top:1755px"><div class="svc-photo warm" role="img" aria-label="Photo of a wooden kitchen hallway"></div><div class="svc-band">DUCTLESS REPAIRS</div></div>
  <div class="abs svc" style="left:614px;top:1755px"><div class="svc-photo" role="img" aria-label="Photo of white kitchen cabinets"></div><div class="svc-band">DUCTLESS<br>WARRANTY</div></div>
  <div class="abs svc" style="left:880px;top:1755px"><div class="svc-photo" role="img" aria-label="Photo of a kitchen with island and pendant"></div><div class="svc-band" style="top:136px;height:73px">WHOLE HOUSE<br>DUCTLESS</div></div>

  <div class="abs btn" style="left:527px;top:2060px;width:174px;height:40px">More Ductless Services</div>
</section>

<section>
  <h2 class="abs section-title" style="top:2180px">Why Shooing Us</h2>

  <div class="abs why" style="left:157px;top:2245px">
    <svg width="60" height="60" viewBox="0 0 60 60"><circle cx="30" cy="30" r="28" fill="none" stroke="#f6c9d6" stroke-width="2"/><rect x="18" y="19" width="24" height="22" rx="3" fill="var(--pink)"/><rect x="28" y="26" width="11" height="8" fill="#fff"/></svg>
    <div class="why-rule" style="background:var(--pink)"></div>
    <div class="why-title">0% Financing For 60 Mounth</div>
    <div class="why-text">Providing options to our customers where it matters most. Offer applies to Corvane systems.</div>
  </div>

  <div class="abs why" style="left:475px;top:2295px">
    <svg width="60" height="60" viewBox="0 0 60 60"><circle cx="30" cy="30" r="28" fill="none" stroke="var(--yellow)" stroke-width="2"/><path d="M20 28 A10 10 0 0 1 38 24 M40 32 A10 10 0 0 1 22 36" fill="none" stroke="var(--yellow)" stroke-width="3"/><path d="M38 18 L39 25 L32 25 Z M22 42 L21 35 L28 35 Z" fill="var(--yellow)"/></svg>
    <div class="why-rule" style="background:var(--yellow)"></div>
    <div class="why-title">356 Day Money Back Guarantee</div>
    <div class="why-text">Providing options to our customers where it matters most. Offer applies to Corvane systems.</div>
  </div>

  <div class="abs why" style="left:800px;top:2245px">
    <svg width="60" height="60" viewBox="0 0 60 60"><circle cx="30" cy="30" r="28" fill="none" stroke="var(--blue)" stroke-width="3"/><rect x="18" y="15" width="24" height="30" rx="3" fill="var(--blue)"/><circle cx="30" cy="26" r="5" fill="#fff"/><path d="M22 39 Q30 29 38 39 Z" fill="#fff"/></svg>
    <div class="why-title" style="margin-top:22px">We Are The Experts of<br>Ductless Services</div>
    <div class="why-text" style="margin-top:16px">Providing options to our customers where it matters most. Offer applies to Corvane systems.</div>
  </div>
</section>

<section>
  <div class="abs testi" role="img" aria-label="Photo of a clean white kitchen"></div>
  <div class="abs testi-shade"></div>
  <p class="abs testi-quote">“The Install Is Clean And Looks Great”</p>
  <div class="abs avatar" role="img" aria-label="Customer portrait"></div>
  <div class="abs testi-name">Marisol T.</div>
  <svg class="abs" style="left:42px;top:2765px" width="20" height="32" viewBox="0 0 20 32"><path d="M17 2 L3 16 L17 30" fill="none" stroke="#fff" stroke-width="3"/></svg>
  <svg class="abs" style="left:1125px;top:2765px" width="20" height="32" viewBox="0 0 20 32"><path d="M3 2 L17 16 L3 30" fill="none" stroke="#fff" stroke-width="3"/></svg>
  <div class="abs dot" style="left:551px;background:#fff"></div>
  <div class="abs dot" style="left:584px"></div>
  <div class="abs dot" style="left:617px"></div>
</section>

<section>
  <p class="abs more-kicker">SEE OTHER WAYS WE CAN HELP WITH YOUR DUCTLESS SYSTEMS</p>
  <div class="abs more-rule"></div>
  <h2 class="abs more-title">We Stand Behind Our Ductless Services</h2>

  <div class="abs card" style="left:185px;top:3236px">
    <div class="card-photo" role="img" aria-label="Photo of a person working on a laptop" style="background:linear-gradient(135deg,#dfe3e6,#8fa2b8 60%,#4d6a8e)"></div>
    <div class="card-title">GET SOME ANSWERS</div>
    <div class="btn card-btn">DUCTLESS FAQ</div>
  </div>
  <div class="abs card" style="left:482px;top:3236px">
    <div class="card-photo" role="img" aria-label="Photo of coins spilling from a jar" style="background:linear-gradient(135deg,#6b3b22,#b87a52 50%,#3a2116)"></div>
    <div class="card-title">TOUR FINANCING OPTION</div>
    <div class="btn card-btn">FINANCING</div>
  </div>
  <div class="abs card" style="left:778px;top:3238px">
    <div class="card-photo" role="img" aria-label="Photo of a bright kitchen with range hood" style="background:linear-gradient(180deg,#e9e6e1,#c9c3ba 60%,#8e877d)"></div>
    <div class="card-title">TOUR FINANCING OPTION</div>
    <div class="btn card-btn" style="width:120px">OUR BLOG</div>
  </div>
</section>

<footer>
  <div class="abs footer"></div>
  <div class="abs foot-brand"><span class="brand-dot"></span>Amber Kite</div>
  <div class="abs foot-col" style="left:663px;top:3688px">
    <h4>QUIK LiNKS</h4>
    Home<br>About Us<br>Ductless Heat Pumps<br>FAQ<br>Financing<br>Reviews<br>Contact Us
  </div>
  <div class="abs foot-col" style="left:926px;top:3688px">
    <h4>Follow Us</h4>
    Hivepage<br>Snapfolio<br>Chirpline<br>Workmesh<br>999 999 9999
  </div>
</footer>
</body>
</html>
```